RedField - Rebranding, Namecard, Stationary and One Page Web

Refresh logo, make it modern and design matching name card, stationary and one page web

RedField Information Technology (Int'l) Company Limited
紅原訊息科技(國際)有限公司

Company is System Integrator, and will be providing products and services to government and enterprise organizations. Our Chief Security Officer came from top U.S. vendor, and had been working on top enterprise and government projects globally, so we want the refreshed image of the new company to have a East Cost U.S. style, with hint of technology from Silicon Valley. The company will also be representing top brands from the U.S. on information security.

Branding refresh is needed because company is being acquired and is expanding

Target Market(s)

Cyber Security

Industry/Entity Type

Information Technology

Contact Information for Business Card

Need Chinese and English

Number of Pages Required

1 page

Font styles to use
Sans Serif

Colors
0292cd
00a990

Requirements
Must have
• Modern, clean, cyber look. Must keep same colors and general look and feel of original logo. Only modernization, do not change its personality

```html
<!DOCTYPE html>
<html lang="en">
<head>
<meta charset="utf-8">
<title>RedField Name Card</title>
<link rel="stylesheet" href="https://fonts.googleapis.com/css2?family=Roboto:wght@300;400;700;900&family=Noto+Sans+TC:wght@400;500&display=swap">
<style>
  :root {
    --brand-blue: #0292cd;
    --brand-teal: #00a990;
    --backdrop: #2b2b2d;
    --card-light: #4a4a4d;
    --card-dark: #2a2a2c;
    --text-light: #e6e6e6;
    --text-muted: #b8b8b8;
    --rule: #8a8a8a;
  }
  * { margin: 0; padding: 0; box-sizing: border-box; }
  html, body { width: 1200px; height: 900px; overflow: hidden; }
  body {
    background: var(--backdrop);
    font-family: "Roboto", "Noto Sans TC", sans-serif;
    position: relative;
  }
  .card {
    position: absolute;
    border-radius: 22px;
    background: radial-gradient(ellipse at 55% 40%, var(--card-light), var(--card-dark) 80%);
    box-shadow: 0 18px 40px rgba(0,0,0,.55);
  }
  .card-front { left: 120px; top: 110px; width: 460px; height: 262px; }
  .card-back  { left: 600px; top: 360px; width: 500px; height: 286px; }

  .wordmark {
    font-family: "Roboto", sans-serif;
    font-weight: 900;
    color: var(--brand-blue);
    letter-spacing: -0.5px;
    line-height: 1;
    display: flex;
    align-items: center;
    gap: 8px;
  }
  .wordmark-dot {
    width: 12px; height: 12px; border-radius: 50%;
    background: var(--brand-teal);
  }
  .front-lockup {
    position: absolute; left: 50%; top: 50%;
    transform: translate(-50%, -50%);
    text-align: left;
  }
  .front-lockup .wordmark { font-size: 54px; }
  .lockup-sub {
    margin-top: 6px;
    font-size: 9px;
    color: var(--brand-blue);
    line-height: 1.35;
  }
  .lockup-sub .zh { font-family: "Noto Sans TC", sans-serif; font-size: 10px; }

  .back-heading {
    position: absolute; right: 28px; top: 26px; text-align: left;
    color: var(--text-light);
  }
  .back-heading .zh {
    font-family: "Noto Sans TC", sans-serif; font-size: 21px; letter-spacing: 1px;
  }
  .back-heading .en { font-size: 11.5px; font-weight: 300; color: var(--text-muted); margin-top: 2px; }

  .back-logo { position: absolute; left: 30px; top: 128px; }
  .back-logo .wordmark { font-size: 32px; }

  .person { position: absolute; right: 290px; top: 208px; text-align: right; }
  .person-name { font-size: 18px; font-weight: 300; color: var(--text-light); letter-spacing: .5px; }
  .person-name .surname { color: var(--brand-blue); }
  .person-title { font-size: 12px; font-weight: 300; color: var(--text-light); margin-top: 2px; }

  .divider {
    position: absolute; left: 226px; top: 120px; width: 1px; height: 142px;
    background: var(--rule);
  }
  .contact {
    position: absolute; left: 240px; top: 122px; width: 250px;
    font-size: 9px; font-weight: 300; color: var(--text-light); line-height: 1.5;
  }
  .contact-row { display: flex; gap: 10px; margin-bottom: 4px; }
  .contact-label { width: 40px; flex: none; color: var(--text-muted); }
  .contact-zh { font-family: "Noto Sans TC", sans-serif; margin: 4px 0 8px 50px; }

  .logo-lockup { position: absolute; left: 840px; top: 760px; }
  .logo-lockup .wordmark { font-size: 64px; }
  .logo-lockup .lockup-sub { font-size: 10px; margin-top: 4px; }
  .logo-lockup .lockup-sub .zh { font-size: 12px; }
</style>
</head>
<body>

  <section class="card card-front" aria-label="Name card front">
    <div class="front-lockup">
      <div class="wordmark">RedField<span class="wordmark-dot"></span></div>
      <div class="lockup-sub">
        <div class="zh">紅原訊息科技(國際)有限公司</div>
        <div>Information Technology (Int'l) Company Limited</div>
      </div>
    </div>
  </section>

  <section class="card card-back" aria-label="Name card back">
    <header class="back-heading">
      <div class="zh">紅原訊息科技(國際)有限公司</div>
      <div class="en">Information Technology (Int'l) Company Limited</div>
    </header>

    <div class="back-logo"><div class="wordmark">RedField</div></div>

    <div class="person">
      <div class="person-name">KEVIN <span class="surname">LAU</span></div>
      <div class="person-title">CEO</div>
    </div>

    <div class="divider"></div>

    <div class="contact">
      <div class="contact-row"><span class="contact-label">Email</span><span>kevinlau@hkredfield.com.hk</span></div>
      <div class="contact-row"><span class="contact-label">Office</span><span>Room B, Unit 418, 4/F, Lai Tak Ind. Bldg,<br>No. 12 Sheung Yuet Road, Kowloon Bay, Kowloon, HKSAR</span></div>
      <div class="contact-zh">九龍灣上悅道12號 禮德工業大廈 4樓 418-B</div>
      <div class="contact-row"><span class="contact-label">Mobile</span><span>(852) 5210 4786</span></div>
      <div class="contact-row"><span class="contact-label">Website</span><span>www.hkredfield.com.hk</span></div>
    </div>
  </section>

  <div class="logo-lockup" aria-label="RedField logo">
    <div class="wordmark">RedField<span class="wordmark-dot"></span></div>
    <div class="lockup-sub">
      <div class="zh">紅原訊息科技(國際)有限公司</div>
      <div>Information Technology (Int'l) Company Limited</div>
    </div>
  </div>

</body>
</html>
```